Logo Tweak & Full Set of Stationery

We need a redesign / tweaking of Logo for rebranding of our company. We are Australia's largest installer of commercial fencing and high security infrastructure. We also have divisions in security and civil works (infrastrucuture).

We would like to see designs that incorporate black, white & blue. Revamp of current Diamond Logo (including HC) would be ideal but open to all ideas.

Design needs to portray a highly professional & corporate image.

Required:
- Tweak / Redesign of Logo
- Letterhead
- email Signature
- Business Cards
- Presentation Folder

Address fields should be interchangeable to accomodate multiple locations.

Website: www.harvillecorp.com.au
Updates

Due to short turn around time for project - Fee increased to $500 AUD Guaranteed

Thanks

Designs are looking good
I have emailed those submitted thus far to the board to start short listing.

Please do not take offence if your design is eliminated as part of this process  - there are so many great concepts and if is difficult to pick between them.

Thanks
Dustin

Target Market(s)

Tier 1 / 2 Builders (ie.. Brick Arch Peter Farley) and Government related bodies

Industry/Entity Type

Security

Requirements
Must have
• Company Name: Harville Corp

Tag Line: Fencing * Security * Civil

Logo

```html
<!DOCTYPE html>
<html lang="en">
<head>
<meta charset="utf-8">
<title>Harville Corp – Business Cards</title>
<link rel="stylesheet" href="https://fonts.googleapis.com/css2?family=Caladea:wght@400;700&family=Arimo:wght@400&display=swap">
<style>
  :root {
    --backdrop: #dfe0e2;
    --navy: #0b4f8a;
    --blue: #1565a6;
    --bright: #1a7dc2;
    --paper: #ffffff;
    --ink: #3a3a3a;
    --grey: #5a5a5a;
    --muted: #8a8a8a;
    --serif: "Caladea", Georgia, serif;
    --sans: "Arimo", Arial, sans-serif;
  }
  * { box-sizing: border-box; margin: 0; padding: 0; }
  html, body { width: 1200px; height: 989px; overflow: hidden; }
  body { background: var(--backdrop); position: relative; font-family: var(--serif); color: var(--ink); }

  .card {
    position: absolute; width: 395px; height: 225px; background: var(--paper);
    box-shadow: 0 2px 6px rgba(0,0,0,.28); overflow: hidden;
  }
  .card-front-a { left: 200px; top: 211px; }
  .card-back-a  { left: 624px; top: 254px; }
  .card-front-b { left: 182px; top: 526px; width: 394px; }
  .card-back-b  { left: 614px; top: 592px; width: 394px; }

  .panel-blue {
    position: absolute;
    background: linear-gradient(120deg, var(--navy), var(--blue) 60%, var(--bright));
    color: var(--paper);
  }

  .brand { position: absolute; display: flex; flex-direction: column; align-items: center; text-align: center; }
  .brand-mark { width: 30px; height: 30px; background: var(--blue); margin-bottom: 8px; }
  .brand-name { font-family: var(--serif); font-weight: 400; font-size: 17px; letter-spacing: .3px; text-transform: uppercase; color: var(--ink); white-space: nowrap; }
  .brand-tag { font-family: var(--sans); font-size: 6.5px; color: var(--blue); margin-top: 1px; white-space: nowrap; }
  .brand.on-blue .brand-mark { background: var(--paper); }
  .brand.on-blue .brand-name, .brand.on-blue .brand-tag { color: var(--paper); }

  .person-name { font-weight: 700; font-size: 15px; line-height: 1.1; }
  .person-role { font-weight: 700; font-size: 11px; line-height: 1.2; }
  .contact { font-size: 11px; line-height: 1.25; white-space: nowrap; }
  .contact .label { display: inline-block; width: 14px; }
  .contact .freecall { color: var(--muted); }

  .services { font-family: var(--sans); font-size: 8.6px; line-height: 1.38; white-space: nowrap; }
</style>
</head>
<body>

  <section class="card card-front-a">
    <div class="panel-blue" style="left:0;top:0;width:224px;height:225px;">
      <div style="position:absolute;right:17px;top:72px;text-align:right;">
        <p class="person-name">Dustin Mercer</p>
        <p class="person-role">Chief Financial Officer</p>
      </div>
      <div class="contact" style="position:absolute;right:17px;top:165px;text-align:right;font-weight:700;">
        <p>M: 0412 555 018</p>
        <p>dmercer@harvillecorp.com.au</p>
        <p>www.harvillecorp.com.au</p>
      </div>
    </div>
    <div class="brand" style="left:236px;top:32px;width:150px;">
      <span class="brand-mark"></span>
      <span class="brand-name" style="font-size:15px;">Harville Corp</span>
      <span class="brand-tag">Fencing • Security • Civil</span>
    </div>
    <div class="contact" style="position:absolute;left:244px;top:165px;color:var(--ink);">
      <p><span class="label">P:</span> +61 2 5550 1146</p>
      <p><span class="label">F:</span> +61 2 5550 1175</p>
      <p class="freecall">Free Call: 1800 555 210</p>
    </div>
  </section>

  <section class="card card-back-a">
    <div class="panel-blue" style="left:0;top:0;width:171px;height:225px;">
      <div class="brand on-blue" style="left:0;top:38px;width:171px;">
        <span class="brand-mark"></span>
        <span class="brand-name" style="font-size:15px;">Harville Corp</span>
        <span class="brand-tag">Fencing • Security • Civil</span>
      </div>
      <p style="position:absolute;left:4px;right:4px;top:160px;text-align:center;font-size:10.5px;line-height:1.25;white-space:nowrap;">
        <b>Harville Corp</b> specialises<br>in all types of commercial<br>fencing and security systems
      </p>
    </div>
    <p class="services" style="position:absolute;left:184px;top:28px;color:var(--grey);">
      Palisade Fencing • Tubular security Fencing<br>HV358 Security Mesh • Chainwire Fencing -<br>both permanent &amp; temporary • Guard Rails<br>&amp; Handrails • Internal Chainwire Enclosures<br>Weldmesh Fencing &amp; Enclosures • Sporting<br>screens &amp; Enclosures • Non-Destructive<br>Digging • Livestock &amp; Fauna Fencing
    </p>
    <p class="services" style="position:absolute;left:184px;top:150px;color:var(--blue);font-size:8.2px;">
      Access Control • Security Systems • Bollards<br>Security Lighting • Alarm Systems • Civil Works<br>Type 1-6 RTA approved Pedestrian Fencing<br>Wire Rope Vehicle Fencing • Rock Fall Fencing<br>Electronic Fencing • All Style of Gates to suit
    </p>
  </section>

  <section class="card card-front-b">
    <div class="brand" style="left:8px;top:58px;width:170px;">
      <span class="brand-mark" style="width:36px;height:36px;"></span>
      <span class="brand-name">Harville Corp</span>
      <span class="brand-tag">Fencing • Security • Civil</span>
    </div>
    <div style="position:absolute;left:205px;top:36px;">
      <p class="person-name" style="color:var(--ink);">Dustin Mercer</p>
      <p class="person-role" style="color:var(--blue);">Chief Financial Officer</p>
    </div>
    <div class="contact" style="position:absolute;left:205px;top:104px;">
      <p><span class="label">M:</span> 0412 555 018</p>
      <p><span class="label">P:</span> +61 2 5550 1146</p>
      <p><span class="label">F:</span> +61 2 5550 1175</p>
      <p class="freecall">Free Call: 1800 555 210</p>
      <p style="margin-top:10px;font-weight:700;">dmercer@harvillecorp.com.au</p>
      <p style="font-weight:700;">www.harvillecorp.com.au</p>
    </div>
    <div class="panel-blue" style="left:0;bottom:0;width:100%;height:17px;"></div>
  </section>

  <section class="card card-back-b">
    <div class="panel-blue" style="left:0;top:0;width:100%;height:165px;">
      <div class="brand on-blue" style="left:0;top:34px;width:100%;">
        <span class="brand-mark" style="width:40px;height:40px;margin-bottom:12px;"></span>
        <span class="brand-name" style="font-size:20px;">Harville Corp</span>
        <span class="brand-tag" style="font-size:9px;">Fencing • Security • Civil</span>
      </div>
    </div>
    <p class="services" style="position:absolute;left:0;right:0;top:177px;text-align:center;color:var(--grey);font-size:8.3px;">
      Access Control • Security Systems • Bollards • Security Lighting • Alarm Systems<br>Civil Works • Type 1-6 RTA approved Pedestrian Fencing • Wire Rope Vehicle Fencing<br>Rock Fall Fencing • Electronic Fencing • All Style of Gates to suit
    </p>
  </section>

</body>
</html>
```